A new healing and spiritual podcast needs a design.

We need a design for the podcast that will also be used on the supporting website. The name is Still Lantern Path. The podcast will be about tapping into our own guidance to have a great life. There will be interviews, meditations, discussions on all aspects of energy healing and alternative healing techniques. The website will be where classes will be offered. Looking for something that conveys a peaceful feeling without looking too "healy-feely". Yet also want it to get peoples attention.

Target Market(s)

Metaphysical, spiritual (not religious), energy healers

Font styles to use
Serif

Requirements
Must have
• The name "Still Lantern Path"
Nice to have
• I'd like it to be inviting, catch peoples eye, convey a peaceful feeling, yet not be boring.
Should not have
• Animated (like comic strip) images.

```html
<!DOCTYPE html>
<html lang="en">
<head>
<meta charset="utf-8">
<title>Still Lantern Path</title>
<link rel="stylesheet" href="https://fonts.googleapis.com/css2?family=Josefin+Sans:wght@400;700&display=swap">
<style>
  :root {
    --paper: #ffffff;
    --mist: #f2f2f2;
    --ink: #161616;
    --crimson: #c3161d;
    --coral: #ef4b53;
    --coral-deep: #c8191f;
    --dusk-sky: #9aa3a6;
    --dusk-water: #2a2a2a;
    --sun-glow: #f7c477;
    --sun-core: #fff1cf;
    --haze: #d8ccc6;
    --earth: #3b2a1c;
  }
  html, body {
    margin: 0;
    padding: 0;
    overflow: hidden;
    background: var(--paper);
  }
  .canvas {
    position: relative;
    width: 1200px;
    height: 1200px;
    overflow: hidden;
    background: var(--paper);
  }
  .artwork {
    position: absolute;
    inset: 0;
    width: 1200px;
    height: 1200px;
  }
  .title {
    position: absolute;
    left: 0;
    right: 0;
    top: 900px;
    margin: 0;
    text-align: center;
    font-family: "Josefin Sans", sans-serif;
    line-height: 1;
  }
  .title__lead {
    display: block;
    font-weight: 400;
    font-size: 98px;
    color: var(--ink);
    letter-spacing: 1px;
  }
  .title__accent {
    display: block;
    margin-top: 22px;
    font-weight: 700;
    font-size: 100px;
    color: var(--crimson);
    letter-spacing: 4px;
    text-transform: uppercase;
  }
</style>
</head>
<body>
<main class="canvas">
  <svg class="artwork" viewBox="0 0 1200 1200" xmlns="http://www.w3.org/2000/svg">
    <defs>
      <linearGradient id="dusk-lake" x1="0" y1="0" x2="0" y2="1">
        <stop offset="0" stop-color="var(--dusk-sky)"/>
        <stop offset="0.3" stop-color="#5c5d58"/>
        <stop offset="0.45" stop-color="#1c1c18"/>
        <stop offset="1" stop-color="var(--dusk-water)"/>
      </linearGradient>
      <linearGradient id="coral-veil" x1="0" y1="0" x2="0" y2="1">
        <stop offset="0" stop-color="var(--coral)"/>
        <stop offset="1" stop-color="var(--coral-deep)"/>
      </linearGradient>
      <radialGradient id="sunset-lake" cx="0.42" cy="0.4" r="0.75">
        <stop offset="0" stop-color="var(--sun-core)"/>
        <stop offset="0.22" stop-color="var(--sun-glow)"/>
        <stop offset="0.55" stop-color="#b07a45"/>
        <stop offset="1" stop-color="var(--earth)"/>
      </radialGradient>
      <linearGradient id="haze-drop" x1="0" y1="0" x2="0" y2="1">
        <stop offset="0" stop-color="var(--haze)"/>
        <stop offset="1" stop-color="#eee6df"/>
      </linearGradient>
    </defs>

    <g class="backdrop" fill="var(--mist)">
      <path d="M90 110 C200 20 420 40 560 60 C700 80 760 40 900 40 C1080 40 1180 150 1160 330 C1140 520 1180 700 1100 860 C1020 1010 900 1080 760 1120 C600 1160 420 1130 300 1060 C170 990 60 930 40 780 C20 620 20 220 90 110Z"/>
    </g>

    <g class="drops">
      <path class="drop drop--coral" fill="var(--coral)" d="M650 90 C665 65 700 70 708 100 C716 130 700 160 680 162 C655 165 640 120 650 90Z"/>
      <path class="drop drop--haze" fill="url(#haze-drop)" d="M580 180 C600 145 660 140 690 170 C720 200 715 280 680 298 C640 315 590 280 575 240 C568 220 570 198 580 180Z"/>
      <path class="drop drop--coral" fill="var(--coral-deep)" d="M1030 735 C1050 690 1100 650 1135 660 C1160 670 1150 720 1120 750 C1090 780 1040 790 1025 770 C1018 760 1022 748 1030 735Z"/>
    </g>

    <g class="photo photo--lake" stroke="var(--paper)" stroke-width="8" role="img" aria-label="Dusky lake with a dark tree-lined shore">
      <path fill="url(#dusk-lake)" d="M85 330 C95 270 200 235 290 228 C345 224 375 250 350 285 C320 330 240 380 215 430 C200 460 140 470 100 455 C70 440 78 370 85 330Z"/>
      <ellipse fill="#3a3a38" cx="86" cy="492" rx="34" ry="18" transform="rotate(-15 86 492)"/>
      <path fill="url(#dusk-lake)" d="M60 540 C70 490 120 475 165 490 C205 505 215 570 245 640 C275 710 320 760 300 800 C280 830 180 825 120 790 C60 750 50 600 60 540Z"/>
    </g>

    <path class="photo photo--veil" fill="url(#coral-veil)" stroke="var(--paper)" stroke-width="8" role="img" aria-label="Lake and hills seen through a red tint" d="M250 330 C320 260 430 245 530 255 C640 265 700 330 680 400 C660 460 560 510 490 600 C455 650 470 720 460 770 C450 810 380 810 320 780 C240 740 200 640 215 520 C222 450 215 370 250 330Z"/>

    <path class="photo photo--meditation" fill="url(#sunset-lake)" stroke="var(--paper)" stroke-width="8" role="img" aria-label="Person meditating cross-legged on a mat by a lake at sunset" d="M720 120 C740 60 880 50 980 90 C1080 130 1150 250 1155 420 C1160 600 1090 780 920 835 C780 880 560 850 490 760 C430 680 470 580 560 500 C640 430 700 330 710 250 C715 190 705 160 720 120Z"/>
  </svg>

  <h1 class="title">
    <span class="title__lead">Still Lantern</span>
    <span class="title__accent">Path</span>
  </h1>
</main>
</body>
</html>
```